Koru upkeep TV Solar Solution

Solar power system install
Services and maintenance
wiring, Rewinding and Renovation
Switch Board Upgrade
Power and lighting point
t doesn’t matter how much you spend on quality parts, your solar system will let you down if your design and installation are sub-par. Have your solar system tailored and installed by our Master Electrician and Bright Grid Guild Accredited team.

Target Market(s)

sales and installed

Industry/Entity Type

Solar install and retailer

Contact Information for Business Card

Name , Email, Phone Number ,Business address,

Font styles to use
Serif

Colors
0054AA
0677BA
7BADD7
CADEEF
E8F1F8

Requirements
Must have
• clear and bright
Nice to have
• new design
Should not have
• unclear pictures

```html
<!DOCTYPE html>
<html lang="en">
<head>
<meta charset="utf-8">
<title>TV Solar Solution – Business Card</title>
<link rel="stylesheet" href="https://fonts.googleapis.com/css2?family=Montserrat:wght@300;400;500;600;700;800&display=swap">
<style>
  :root {
    --blue-deep: #0054AA;
    --blue: #0677BA;
    --blue-soft: #7BADD7;
    --blue-pale: #CADEEF;
    --blue-mist: #E8F1F8;
    --ink: #3d4f63;
    --paper: #ffffff;
    --stage: #e4e5e7;
  }
  * { margin: 0; padding: 0; box-sizing: border-box; }
  html, body { width: 1200px; height: 1200px; overflow: hidden; }
  body {
    background: var(--stage);
    font-family: "Montserrat", Arial, sans-serif;
    position: relative;
  }
  .card {
    position: absolute;
    left: 214px;
    width: 774px;
    height: 441px;
    background: var(--paper);
    overflow: hidden;
  }
  .card--front { top: 107px; }
  .card--back { top: 620px; }

  /* Front */
  .splash { position: absolute; left: 0; top: 0; }
  .splash-services {
    position: absolute;
    left: 390px; top: 30px; width: 374px;
    text-align: center;
    color: #fff;
    font-weight: 600;
    font-size: 18px;
    line-height: 23px;
  }
  .brand {
    position: absolute;
    left: 40px; top: 104px; width: 330px;
    text-align: center;
  }
  .brand-square {
    width: 80px; height: 80px;
    margin: 0 auto 18px;
    border: 3px solid var(--blue-soft);
  }
  .brand-name {
    color: var(--blue-deep);
    font-weight: 700;
    font-size: 29px;
    letter-spacing: 0.2px;
  }
  .service-list {
    position: absolute;
    top: 316px;
    list-style: none;
    color: var(--blue-deep);
    font-size: 21px;
    line-height: 26px;
  }
  .service-list--left { left: 54px; width: 320px; }
  .service-list--right { left: 392px; width: 360px; }
  .service-list li {
    position: relative;
    padding-left: 29px;
    margin-bottom: 5px;
  }
  .service-list svg { position: absolute; left: 0; top: 5px; }

  /* Back */
  .accent-bars { position: absolute; left: 46px; top: 58px; display: flex; gap: 10px; }
  .accent-bars span { display: block; width: 44px; height: 4px; border-radius: 2px; background: var(--blue); }
  .accent-bars span + span { background: var(--blue-pale); }
  .person-name {
    position: absolute; left: 44px; top: 70px;
    font-size: 40px; color: var(--blue-deep);
    font-weight: 300; letter-spacing: 0.5px;
    white-space: nowrap;
  }
  .person-name strong { font-weight: 800; }
  .person-role {
    position: absolute; left: 45px; top: 112px;
    font-size: 18px; color: var(--blue-soft);
  }
  .contact-list { position: absolute; left: 44px; top: 0; list-style: none; }
  .contact-item {
    position: absolute; left: 0;
    display: flex; align-items: center;
    width: 360px;
    color: var(--ink); font-size: 19px; line-height: 26px;
  }
  .contact-icon {
    flex: 0 0 36px; width: 36px; height: 36px;
    border-radius: 50%; background: var(--blue);
    display: flex; align-items: center; justify-content: center;
    margin-right: 14px;
  }
  .photo { position: absolute; left: 0; top: 0; }
</style>
</head>
<body>

<section class="card card--front">
  <svg class="splash" width="774" height="441" viewBox="0 0 774 441" aria-hidden="true">
    <path d="M330 0 C 300 60 340 120 360 170 C 390 240 470 280 580 282 C 690 284 760 230 774 160 L774 0 Z" fill="var(--blue)"/>
  </svg>
  <div class="splash-services">
    <p>Solar power system install</p>
    <p>Services and maintenance</p>
    <p>wiring, Rewinding and Renovation</p>
    <p>Switch Board Upgrade</p>
    <p>Power and lighting point</p>
  </div>

  <div class="brand">
    <div class="brand-square"></div>
    <p class="brand-name">TV Solar Solution</p>
  </div>

  <ul class="service-list service-list--left">
    <li><svg width="17" height="17" viewBox="0 0 17 17"><rect x="1" y="1" width="15" height="15" fill="none" stroke="currentColor" stroke-width="1.6"/><path d="M8.5 1v15M1 8.5h15" stroke="currentColor" stroke-width="1.6"/></svg>Solar power system install</li>
    <li><svg width="17" height="17" viewBox="0 0 17 17"><rect x="1" y="1" width="15" height="15" fill="none" stroke="currentColor" stroke-width="1.6"/><path d="M8.5 1v15M1 8.5h15" stroke="currentColor" stroke-width="1.6"/></svg>wiring, Rewinding and Renovation</li>
  </ul>
  <ul class="service-list service-list--right">
    <li><svg width="17" height="17" viewBox="0 0 17 17"><rect x="1" y="1" width="15" height="15" fill="none" stroke="currentColor" stroke-width="1.6"/><path d="M8.5 1v15M1 8.5h15" stroke="currentColor" stroke-width="1.6"/></svg>Services and maintenance</li>
    <li><svg width="17" height="17" viewBox="0 0 17 17"><rect x="1" y="1" width="15" height="15" fill="none" stroke="currentColor" stroke-width="1.6"/><path d="M8.5 1v15M1 8.5h15" stroke="currentColor" stroke-width="1.6"/></svg>Switch Board Upgrade</li>
    <li><svg width="17" height="17" viewBox="0 0 17 17"><rect x="1" y="1" width="15" height="15" fill="none" stroke="currentColor" stroke-width="1.6"/><path d="M8.5 1v15M1 8.5h15" stroke="currentColor" stroke-width="1.6"/></svg>Power and lighting point</li>
  </ul>
</section>

<section class="card card--back">
  <svg class="photo" width="774" height="441" viewBox="0 0 774 441" role="img" aria-label="Photo of a yellow hard hat resting on solar panels">
    <defs>
      <linearGradient id="photoTone" x1="0" y1="0" x2="1" y2="1">
        <stop offset="0" stop-color="#c9a58f"/>
        <stop offset="0.45" stop-color="#8f8a86"/>
        <stop offset="0.7" stop-color="#c9a92a"/>
        <stop offset="1" stop-color="#3b4149"/>
      </linearGradient>
    </defs>
    <path d="M440 0 C 400 80 420 150 390 210 C 360 280 430 360 500 441 L774 441 L774 0 Z" fill="url(#photoTone)"/>
    <path d="M440 0 C 400 80 420 150 390 210 C 360 280 430 360 500 441" fill="none" stroke="var(--blue)" stroke-width="14"/>
  </svg>

  <div class="accent-bars"><span></span><span></span></div>
  <h1 class="person-name">DANA <strong>HOLT</strong></h1>
  <p class="person-role">Founder &amp; CEO</p>

  <ul class="contact-list">
    <li class="contact-item" style="top:211px">
      <span class="contact-icon"><svg width="18" height="18" viewBox="0 0 24 24"><path d="M6.6 10.8a15.1 15.1 0 0 0 6.6 6.6l2.2-2.2c.3-.3.7-.4 1-.2 1.1.4 2.3.6 3.6.6.6 0 1 .4 1 1V20c0 .6-.4 1-1 1A17 17 0 0 1 3 4c0-.6.4-1 1-1h3.5c.6 0 1 .4 1 1 0 1.3.2 2.5.6 3.6.1.3 0 .7-.2 1z" fill="#fff"/></svg></span>
      555 0148 2290
    </li>
    <li class="contact-item" style="top:259px">
      <span class="contact-icon"><svg width="18" height="18" viewBox="0 0 24 24"><path d="M2 11 22 3l-6 18-4-8z" fill="#fff"/><path d="M12 13 22 3" stroke="var(--blue)" stroke-width="1.5"/></svg></span>
      hello@tvsolar.example
    </li>
    <li class="contact-item" style="top:305px">
      <span class="contact-icon"><svg width="18" height="18" viewBox="0 0 24 24"><path d="M12 2a7 7 0 0 0-7 7c0 5 7 13 7 13s7-8 7-13a7 7 0 0 0-7-7z" fill="#fff"/><circle cx="12" cy="9" r="2.6" fill="var(--blue)"/></svg></span>
      <span>42 Harbour Lane, Suite 7,<br>Westfield, FL 30001</span>
    </li>
    <li class="contact-item" style="top:367px">
      <span class="contact-icon"><svg width="16" height="16" viewBox="0 0 24 24"><path d="M4 4l16 6-7 2-2 7z" fill="#fff"/></svg></span>
      www.tvsolar.example
    </li>
  </ul>
</section>

</body>
</html>
```